Store Promo Card (already have logo!)

I need a card design (single side) for my online women’s gift shop containing a promotional code to be placed in bags for attendees at an event. I’m flexible on both shape and sizing, but perhaps a 4x6 card.
—It should contain my attached logo, my website (www.corvidtpq.com), and my Instagram handle (@corvidtpq) and promotion language such as “15% off your purchase with code: MIRVOL”.
—I think I would like my logo to be large.
—It should be clean, simple and modern in design and should use the colors from my logo.
—I would like about 3-5 product pictures depending on design.
Target Market(s)
Women ages 30 to 60
Industry/Entity Type
Retail Upscale Gift
Look and feel

```html
<!DOCTYPE html>
<html lang="en">
<head>
<meta charset="utf-8">
<title>Corvid TPQ – Promo Card</title>
<link rel="stylesheet" href="https://fonts.googleapis.com/css2?family=Abril+Fatface&display=swap">
<style>
  :root {
    --ink: #5d605f;
    --rose-light: #fbe6e8;
    --rose-mid: #f2c4c9;
    --rose-deep: #e2a2aa;
    --rose-blush: #f8d8dc;
    --pattern-base: #d9d8da;
    --pattern-spot: #7d7f80;
    --glow: rgba(255, 255, 255, 0.85);
  }
  * { margin: 0; padding: 0; box-sizing: border-box; }
  html, body { width: 1200px; height: 800px; overflow: hidden; background: #ffffff; }
  .promo-card {
    position: relative;
    width: 1200px;
    height: 800px;
    overflow: hidden;
    font-family: "Abril Fatface", "Didot", serif;
    color: var(--ink);
  }
  .rose-photo {
    position: absolute;
    inset: 0;
    background:
      radial-gradient(ellipse 420px 360px at 420px 420px, var(--rose-deep) 0%, var(--rose-mid) 45%, transparent 80%),
      radial-gradient(ellipse 380px 420px at 950px 330px, var(--rose-mid) 0%, var(--rose-blush) 55%, transparent 85%),
      linear-gradient(160deg, var(--rose-light) 0%, var(--rose-blush) 50%, var(--rose-light) 100%);
  }
  .pattern-strip {
    position: absolute;
    left: 0; top: 0;
    width: 160px; height: 800px;
    background: linear-gradient(90deg, var(--pattern-spot) 0%, var(--pattern-base) 45%, rgba(217, 216, 218, 0) 100%);
    opacity: 0.75;
  }
  .edge-vignette {
    position: absolute;
    inset: 0;
    box-shadow: inset 0 0 40px rgba(255, 255, 255, 0.9);
    pointer-events: none;
  }
  .headline, .brand-name, .offer-line, .contact-line {
    position: absolute;
    left: 0; right: 0;
    text-align: center;
    white-space: nowrap;
    text-shadow: 0 0 10px var(--glow), 0 0 4px var(--glow);
  }
  .headline {
    top: 28px;
    font-size: 142px;
    line-height: 1;
    letter-spacing: 2px;
  }
  .brand-name {
    top: 300px;
    font-size: 122px;
    line-height: 1;
    letter-spacing: 1px;
    text-shadow: none;
  }
  .offer-line {
    top: 612px;
    font-size: 37px;
    line-height: 1;
  }
  .contact-line {
    top: 744px;
    display: flex;
    justify-content: center;
    align-items: center;
    gap: 48px;
    font-size: 25px;
    line-height: 1;
  }
  .social-handle { display: inline-flex; align-items: center; gap: 6px; }
  .social-dot { width: 26px; height: 26px; display: block; }
</style>
</head>
<body>
  <main class="promo-card">
    <div class="rose-photo" role="img" aria-label="Close-up photograph of soft pink roses filling the card"></div>
    <div class="pattern-strip" role="img" aria-label="Grey leopard-print pattern band along the left edge"></div>
    <div class="edge-vignette"></div>

    <h1 class="headline">15% OFF</h1>
    <p class="brand-name">CORVID TPQ</p>
    <p class="offer-line">YOUR PURCHASE WITH CODE: MIRVOL</p>
    <p class="contact-line">
      <span class="website">WWW.CORVIDTPQ.COM</span>
      <span class="social-handle">
        <svg class="social-dot" viewBox="0 0 26 26" aria-hidden="true"><circle cx="13" cy="13" r="12" fill="var(--ink)"/></svg>
        @CORVIDTPQ
      </span>
    </p>
  </main>
</body>
</html>
```